Harbor Relay Group Letterhead Design

The project name sums it up. Just need a professional letterhead design / template we can use in our marketing folders.

Here's the address / contact info for the letterhead: Harbor Relay Group 4815 Maple Crest Ave Suite 210 Brookhaven Falls, Oregon 77419 555-507-3846 www.harborrelaygroup.us support@harborrelaygroup.us

```html
<!DOCTYPE html>
<html lang="en">
<head>
<meta charset="utf-8">
<title>Harbor Relay Group Letterhead</title>
<link rel="stylesheet" href="https://fonts.googleapis.com/css2?family=Open+Sans:wght@400;700&family=Orbitron:wght@800&display=swap">
<style>
  :root {
    --backdrop: #e9e6e2;
    --paper: #ffffff;
    --navy: #0b1020;
    --brand-blue: #2350a3;
    --silver-light: #e4e4e4;
    --silver-dark: #8c8c8c;
    --watermark: #ececec;
    --ink-light: #ffffff;
  }
  html, body {
    margin: 0;
    width: 1200px;
    height: 900px;
    overflow: hidden;
    background: var(--backdrop);
  }
  .canvas {
    position: relative;
    width: 1200px;
    height: 900px;
  }
  .letterhead {
    position: absolute;
    left: 283px;
    top: 41px;
    width: 634px;
    height: 817px;
    background: var(--paper);
    box-shadow: 0 4px 14px rgba(0,0,0,0.18);
    overflow: hidden;
  }
  .masthead {
    position: absolute;
    top: 56px;
    left: 0;
    right: 0;
    display: flex;
    justify-content: center;
    align-items: center;
    gap: 10px;
  }
  .masthead-mark {
    width: 34px;
    height: 34px;
    border-radius: 50%;
    background: var(--brand-blue);
  }
  .masthead-name {
    font-family: "Open Sans", sans-serif;
    font-weight: 700;
    font-size: 26px;
    color: var(--brand-blue);
    letter-spacing: 0.3px;
  }
  .footer-art {
    position: absolute;
    inset: 0;
  }
  .contact-block {
    position: absolute;
    left: 422px;
    top: 708px;
    font-style: normal;
    color: var(--ink-light);
    font-family: "Open Sans", sans-serif;
    font-size: 10.5px;
    line-height: 13.5px;
  }
  .contact-heading {
    font-family: "Orbitron", sans-serif;
    font-weight: 800;
    font-size: 9px;
    letter-spacing: 0.8px;
    color: var(--brand-blue);
    text-transform: uppercase;
  }
  .contact-lines { margin-bottom: 6px; }
  .contact-row {
    display: flex;
    align-items: center;
    gap: 5px;
  }
  .contact-row svg { width: 10px; height: 10px; flex: none; }
</style>
</head>
<body>
<div class="canvas">
  <div class="letterhead">
    <header class="masthead">
      <span class="masthead-mark"></span>
      <span class="masthead-name">Harbor Relay Group</span>
    </header>

    <svg class="footer-art" viewBox="0 0 634 817" width="634" height="817" aria-hidden="true">
      <defs>
        <linearGradient id="silver" x1="0" y1="0" x2="1" y2="0">
          <stop offset="0" stop-color="var(--silver-dark)"/>
          <stop offset="0.5" stop-color="var(--silver-light)"/>
          <stop offset="1" stop-color="var(--silver-dark)"/>
        </linearGradient>
      </defs>
      <circle class="watermark-disc" cx="93" cy="694" r="68" fill="var(--watermark)"/>
      <path class="wave-silver" d="M0 782 C150 784 290 752 410 708 C490 682 560 678 634 680 L634 695 C560 693 495 697 420 720 C300 762 150 794 0 796 Z" fill="url(#silver)"/>
      <path class="wave-navy" d="M0 796 C150 794 300 762 420 720 C495 697 560 693 634 695 L634 817 L0 817 Z" fill="var(--navy)"/>
      <circle class="partner-badge" cx="315" cy="767" r="13" fill="none" stroke="var(--brand-blue)" stroke-width="3"/>
    </svg>

    <address class="contact-block">
      <div class="contact-heading">Harbor Relay Group</div>
      <div class="contact-lines">
        4815 Maple Crest Ave Suite 210<br>
        Brookhaven Falls, Oregon 77419
      </div>
      <div class="contact-row">
        <svg viewBox="0 0 10 10"><path d="M2 0.5 L3.6 2.6 L2.8 3.6 C3.4 5 4.8 6.5 6.3 7.2 L7.3 6.3 L9.5 7.9 L8.4 9.5 C4.5 9.3 0.6 5.4 0.5 1.6 Z" fill="var(--brand-blue)"/></svg>
        <span>555-507-3846</span>
      </div>
      <div class="contact-row">
        <svg viewBox="0 0 10 10"><rect x="0.5" y="2" width="9" height="6.5" fill="var(--brand-blue)"/><path d="M0.5 2 L5 5.5 L9.5 2" fill="none" stroke="var(--navy)" stroke-width="0.9"/></svg>
        <span>support@harborrelaygroup.us</span>
      </div>
      <div class="contact-row">
        <svg viewBox="0 0 10 10"><circle cx="5" cy="5" r="4.5" fill="var(--brand-blue)"/><path d="M0.5 5 H9.5 M5 0.5 C3 3 3 7 5 9.5 M5 0.5 C7 3 7 7 5 9.5" fill="none" stroke="var(--navy)" stroke-width="0.7"/></svg>
        <span>www.harborrelaygroup.us</span>
      </div>
    </address>
  </div>
</div>
</body>
</html>
```